Funky physio needs a business card to match!

We are a physiotherapy clinic and pilates studio who specialise in sports and spinal injuries, as well as persistent or chronic pain.

We would like a vibrant and fun business card which is not over medicalised.
Updates

PO Box number is 418

Industry/Entity Type

Clinic

Contact Information for Business Card

Tidewell Sports Medicine
Suite 3 & 4 Marlowe St, BRINDLECOVE VIC 3468
p 86203917
f 9481 3057
e admin@tidewellsportsmedicine.com.au
w tidewellsportsmedicine.com.au

All correspondence via email or mailed to:
PO Box
BRINDLECOVE VIC 3468

Requirements
Must have
• Must have a green element - see logo. I don't mind if the business card is green, or if it's black, grey, white etc with green highlights. I'm the physio ... you're the designer!!!! It just needs to "look" green!
Our font is Harabara and can be downloaded from glyphbarn.com
Nice to have
• Please check our website to get a feel of our company. We don't take ourselves to seriously, however want to be taken seriously!
Should not have
• not over medicalised or corporate

```html
<!DOCTYPE html>
<html lang="en">
<head>
<meta charset="utf-8">
<title>Tidewell Sports Medicine – Business Card</title>
<link rel="stylesheet" href="https://fonts.googleapis.com/css2?family=Nunito:wght@800&family=Open+Sans:wght@400&display=swap">
<style>
  :root {
    --page: #ffffff;
    --card-edge: #c9c9c9;
    --lime: #80e800;
    --lime-mid: #6fd400;
    --leaf: #4fae00;
    --ring: #5cb800;
    --brand-green: #5fbb0a;
    --mark-fill: #76cc1a;
    --contact-text: #ffffff;
  }
  html, body {
    margin: 0;
    padding: 0;
    width: 1200px;
    height: 680px;
    overflow: hidden;
    background: var(--page);
  }
  .business-card {
    position: relative;
    width: 1200px;
    height: 680px;
  }
  .card-shapes {
    position: absolute;
    inset: 0;
    display: block;
  }
  .brand-name {
    position: absolute;
    left: 52px;
    top: 426px;
    width: 430px;
    margin: 0;
    text-align: center;
    font-family: "Nunito", sans-serif;
    font-weight: 800;
    font-size: 35px;
    letter-spacing: -0.4px;
    color: var(--brand-green);
    white-space: nowrap;
  }
  .contact-details {
    position: absolute;
    left: 562px;
    top: 230px;
    margin: 0;
    font-family: "Open Sans", sans-serif;
    font-weight: 400;
    font-size: 31.5px;
    line-height: 44.5px;
    color: var(--contact-text);
    white-space: nowrap;
  }
  .contact-details span { display: block; }
  .contact-details .divider { display: inline; padding: 0 20px; }
</style>
</head>
<body>
<main class="business-card">
  <svg class="card-shapes" width="1200" height="680" viewBox="0 0 1200 680" aria-hidden="true">
    <defs>
      <linearGradient id="greenSweep" x1="0" y1="0" x2="1" y2="0">
        <stop offset="0.3" stop-color="var(--lime)"/>
        <stop offset="0.65" stop-color="var(--lime-mid)"/>
        <stop offset="1" stop-color="var(--leaf)"/>
      </linearGradient>
      <clipPath id="cardShape">
        <rect x="2" y="2" width="1196" height="676" rx="98" ry="98"/>
      </clipPath>
    </defs>
    <g clip-path="url(#cardShape)">
      <rect class="green-field" x="0" y="0" width="1200" height="680" fill="url(#greenSweep)"/>
      <circle class="white-arc-gap" cx="160" cy="339" r="384" fill="var(--page)"/>
      <circle class="white-panel" cx="160" cy="339" r="378" fill="var(--page)" stroke="var(--ring)" stroke-width="8"/>
      <circle class="white-panel-inner" cx="160" cy="339" r="373" fill="var(--page)"/>
    </g>
    <rect class="card-outline" x="2" y="2" width="1196" height="676" rx="98" ry="98" fill="none" stroke="var(--card-edge)" stroke-width="2"/>
    <circle class="brand-dot" cx="262" cy="292" r="88" fill="var(--mark-fill)"/>
  </svg>

  <p class="brand-name">Tidewell Sports Medicine</p>

  <p class="contact-details">
    <span>P 86203917<span class="divider">|</span>F 9481 3057</span>
    <span>admin@tidewellsportsmedicine.com.au</span>
    <span>tidewellsportsmedicine.com.au</span>
    <span>Suite 3 &amp; 4 Marlowe St,</span>
    <span>Brindlecove VIC 3468</span>
  </p>
</main>
</body>
</html>
```